Lift Her Forward, 2019 Save The Date

Please develop a save the date flyer our 4th Annual Lift Her Forward and See Her Rise! This event is focused on maintaining participation and appreciation for women in the design and construction industry.

This unique Forum provides a venue to engage everyone from executives to those just beginning their careers with active, hands-on sessions and vibrant networking with the best and brightest in the A/E/C industry. In our usual Q-TarVM Forum style, Keynotes become table participants and table participants become presenters, encouraging participants to assimilate what they are learning. Join local, state and national leaders and subject matter experts as we candidly explore and address the issues affecting women in our industry.

Industry/Entity Type

Construction

Font styles to use
Sans Serif

Requirements
Must have
• This is a save the date, Must have:
• Q-TarVM Logo
• Title: 4th Annual Lift Her Forward and See Her Rise!
• Date: January 25, 2019
• Location: Harbor Crest Resort and Spa, San Marcos, TX
Nice to have
• A header that can easily be pulled to add to other marketing materials and for use across other platforms (web, etc.).

```html
<!DOCTYPE html>
<html lang="en">
<head>
<meta charset="utf-8">
<title>Lift Her Forward 2019 – Save the Date</title>
<link rel="stylesheet" href="https://fonts.googleapis.com/css2?family=Barlow:wght@400;500&family=Oswald:wght@600&family=Dancing+Script:wght@600&display=swap">
<style>
  :root {
    --flyer-blue: #2a3f84;
    --ink-white: #ffffff;
  }
  * { margin: 0; padding: 0; box-sizing: border-box; }
  html, body {
    width: 955px;
    height: 1200px;
    overflow: hidden;
    background: var(--flyer-blue);
  }
  .flyer {
    position: relative;
    width: 955px;
    height: 1200px;
    background: var(--flyer-blue);
    color: var(--ink-white);
    font-family: "Barlow", "Helvetica Neue", Arial, sans-serif;
  }
  .event-title {
    position: absolute;
    top: 106px;
    left: 0;
    width: 100%;
    text-align: center;
    font-weight: 500;
    font-size: 23px;
    line-height: 37px;
    letter-spacing: 0.4px;
    text-transform: uppercase;
  }
  .headline {
    position: absolute;
    left: 0;
    top: 0;
    width: 955px;
    height: 760px;
  }
  .headline text.big-word {
    font-family: "Oswald", "Arial Narrow", sans-serif;
    font-weight: 600;
    fill: var(--ink-white);
  }
  .headline text.connector {
    font-family: "Dancing Script", cursive;
    font-weight: 600;
    fill: var(--ink-white);
  }
  .event-date {
    position: absolute;
    top: 746px;
    left: 0;
    width: 100%;
    display: flex;
    justify-content: center;
    align-items: center;
    gap: 14px;
    font-size: 46px;
    font-weight: 400;
    letter-spacing: 0.5px;
  }
  .event-date .day {
    width: 82px;
    height: 82px;
    border-radius: 50%;
    background: var(--ink-white);
    color: var(--flyer-blue);
    font-family: "Oswald", "Arial Narrow", sans-serif;
    font-weight: 600;
    font-size: 44px;
    display: flex;
    align-items: center;
    justify-content: center;
  }
  .venue {
    position: absolute;
    top: 842px;
    left: 181px;
    width: 601px;
    height: 51px;
    border-top: 2px solid var(--ink-white);
    border-bottom: 2px solid var(--ink-white);
    display: flex;
    align-items: center;
    justify-content: center;
    font-size: 23px;
    font-weight: 500;
    letter-spacing: 0.3px;
  }
  .organizer {
    position: absolute;
    top: 1040px;
    left: 0;
    width: 100%;
    display: flex;
    justify-content: center;
    align-items: center;
    gap: 12px;
  }
  .organizer .mark-dot {
    width: 30px;
    height: 30px;
    border-radius: 50%;
    background: var(--ink-white);
  }
  .organizer .name {
    font-size: 40px;
    font-weight: 500;
    letter-spacing: 0.5px;
  }
</style>
</head>
<body>
  <main class="flyer">
    <p class="event-title">4th Annual Lift Her Forward<br>and See Her Rise!</p>

    <svg class="headline" viewBox="0 0 955 760" aria-label="Save the Date">
      <text class="big-word" x="244" y="415" font-size="278" textLength="465" lengthAdjust="spacingAndGlyphs">SAVE</text>

      <rect x="244" y="464" width="40" height="10" rx="5" fill="#ffffff" role="img" aria-label="Leaf flourish ornament"/>
      <line x1="284" y1="469" x2="416" y2="469" stroke="#ffffff" stroke-width="3" stroke-linecap="round"/>
      <text class="connector" x="477" y="481" font-size="42" text-anchor="middle">the</text>
      <line x1="538" y1="469" x2="670" y2="469" stroke="#ffffff" stroke-width="3" stroke-linecap="round"/>
      <rect x="670" y="464" width="40" height="10" rx="5" fill="#ffffff" role="img" aria-label="Leaf flourish ornament"/>

      <text class="big-word" x="244" y="717" font-size="278" textLength="459" lengthAdjust="spacingAndGlyphs">DATE</text>
    </svg>

    <div class="event-date">
      <span class="month">JANUARY</span>
      <span class="day">25</span>
      <span class="year">2019</span>
    </div>

    <p class="venue">Harbor Crest Resort and Spa, San Marcos, TX</p>

    <div class="organizer">
      <span class="mark-dot"></span>
      <span class="name">Q-TarVM</span>
    </div>
  </main>
</body>
</html>
```